We need a website that entices australia's workers to sign up to help protect their industry and their jobs. The key message is "Building a Stronger Australia" and that headline / tagline should feature prominently on the site.

In terms of style I lack the current 'scrolling' style (see example http://www.pebblelane.ca )

The site must dynamically for mobile platforms. It must also use Joomla or Wordpress as CMS so is client editable.

The attached logo is the basis for the design and the name of the organisation is the Enduring Progress Council. Please make an allowance for an iframe embed (min height 650px) see attached sample.

It should also have a subscriber sign up for that connects with Mailing Beacon

Attached text for front page is DRAFT ONLY

Target Market(s)

Working class australians, (eg miners, farmers, factory workers, etc)

Industry/Entity Type

Industry

Coding

Coded - Design and coding required

Number of Pages Required

4 page

Requirements
Must have
• An editable CMS
• Subscription form connecting with Mailing Beacon (see https://kelvoram.postriver.com/help/topic.aspx?t=13)
• Must resize for mobile
• Must allow for an iframe
Nice to have
• It must have a friendly feel but strong, not 'girly' though should not alienate women
Should not have
• Images that are not australian
• Images that do not have the appropriate rights to use

```html
<!DOCTYPE html>
<html lang="en">
<head>
<meta charset="utf-8">
<title>Building a stronger Australia — Enduring Progress Council</title>
<link rel="stylesheet" href="https://fonts.googleapis.com/css2?family=Montserrat:wght@400;500;600&family=Roboto+Slab:wght@400;500&display=swap">
<style>
:root{
  --orange:#fe5309;
  --yellow:#fdba35;
  --ink:#2c3a4a;
  --white:#ffffff;
  --field:#f4f5f7;
  --field-text:#2c3a4a;
  --icon-grey:#8a94a0;
  --slab:"Roboto Slab", Georgia, serif;
  --sans:"Montserrat", Arial, sans-serif;
}
*{box-sizing:border-box;margin:0;padding:0}
html,body{width:1200px;height:3666px;overflow:hidden}
body{font-family:var(--sans);color:var(--white);background:var(--orange);position:relative}
section{position:absolute;left:0;width:1200px;overflow:hidden}
.abs{position:absolute}
.center{left:0;width:1200px;text-align:center}
.photo{position:absolute;inset:0}
.slab-title{font-family:var(--slab);font-weight:500;font-size:56px;line-height:1}

/* hero */
.hero{top:0;height:574px}
.hero .photo{background:radial-gradient(ellipse at 45% 40%,#7d8c9c 0%,#536476 45%,#2f3d4d 100%)}
.brand{left:150px;top:20px;display:flex;align-items:center;gap:12px;font-weight:600;font-size:15px}
.brand-dot{width:26px;height:26px;border-radius:50%;background:var(--orange)}
.main-nav{left:606px;top:33px;display:flex;gap:27px;font-size:15px;font-weight:500}
.menu-toggle{left:1002px;top:27px;width:48px}
.menu-toggle span{display:block;height:5px;background:var(--white);margin-bottom:6px;border-radius:1px}
.hero-title{top:261px;font-size:60px}
.slide-thumb{top:220px}
.slide-thumb.left{left:-10px}
.slide-thumb.right{left:1075px}
.scroll-down{left:569px;top:471px}

/* family */
.family{top:574px;height:575px}
.family h2{top:150px}
.family .lead{top:236px;font-size:25px;line-height:31px;font-weight:400}
.btn{display:flex;align-items:center;justify-content:center;background:var(--yellow);color:var(--white);font-weight:500;font-size:14px}
.family .btn{left:455px;top:357px;width:290px;height:54px}

/* features */
.features{top:1149px;height:621px}
.features .photo{background:linear-gradient(180deg,#3b4b5d 0%,#2e3d4f 55%,#263444 100%)}
.features h2{top:92px}
.features .lead{top:180px;font-size:21px;line-height:28px}
.feature{width:210px;text-align:center}
.feature .hex-wrap{position:relative;width:130px;height:150px;margin:0 auto}
.feature .hex-label{position:absolute;left:0;width:130px;top:95px;font-size:13px;font-weight:500}
.feature p{margin-top:18px;font-size:13px;line-height:19px}

/* about */
.about{top:1770px;height:637px}
.about h2{top:100px}
.video-frame{left:152px;top:222px;width:472px;height:291px;border:5px solid var(--white);background:linear-gradient(180deg,#8aa2b8 0%,#c79a5a 55%,#5a4532 100%)}
.about-copy{left:667px;top:220px;width:372px;font-size:15.5px;line-height:23.5px}
.about-copy p+p{margin-top:23px}
.about .btn{left:667px;top:493px;width:183px;height:42px}

/* email */
.email{top:2407px;height:678px}
.email .photo{background:linear-gradient(180deg,#3e4f62 0%,#2f3f51 50%,#1f2b39 100%)}
.email h2{top:98px}
.email .lead{left:215px;width:770px;top:180px;font-size:20px;line-height:26px;text-align:center}
.field{height:31px;background:var(--field);color:var(--field-text);font-size:11px;font-weight:600;display:flex;align-items:center;justify-content:space-between;padding:0 10px}
.col-a{left:188px;width:401px}
.col-b{left:609px;width:405px}
.submit{border:2px solid var(--yellow);color:var(--white);font-size:12px;font-weight:500;display:flex;align-items:center;justify-content:center;letter-spacing:.5px}
.divider{left:538px;top:528px;width:124px;height:2px;background:var(--white)}
.social{top:565px;left:507px;display:flex;gap:19px}
.social span{width:22px;height:22px;border-radius:50%;background:var(--white);opacity:.85}

/* contact */
.contact{top:3085px;height:581px}
.contact h2{top:93px;font-family:var(--sans);font-weight:500;font-size:54px}
.contact h3{top:203px;font-size:24px;font-weight:400;letter-spacing:.5px}
.info{width:200px;font-size:9px;line-height:14px}
.info .label{font-weight:600;font-size:10px;margin-top:8px;display:block}
.contact .field{height:32px}
.contact .msg{height:83px;align-items:flex-start;padding-top:10px}
.contact .btn{left:616px;top:417px;width:183px;height:42px}
</style>
</head>
<body>

<section class="hero">
  <div class="photo" role="img" aria-label="Two businesswomen talking in a bright office"></div>
  <div class="abs brand"><span class="brand-dot"></span>Enduring Progress Council</div>
  <nav class="abs main-nav"><span>Take Action</span><span>About</span><span>Facts</span><span>News</span><span>Contact</span></nav>
  <div class="abs menu-toggle"><span></span><span></span><span></span></div>
  <h1 class="abs center slab-title hero-title">Building a stronger Australia</h1>
  <svg class="abs slide-thumb left" width="135" height="140" viewBox="0 0 135 140">
    <polygon points="67,4 129,38 129,102 67,136 5,102 5,38" fill="#7c8fa3" stroke="#fff" stroke-width="3" role="img" aria-label="Preview of previous slide, city skyline"/>
    <circle cx="36" cy="70" r="17" fill="none" stroke="#fff" stroke-width="2.5"/>
    <path d="M40 62 L32 70 L40 78" fill="none" stroke="#fff" stroke-width="3"/>
  </svg>
  <svg class="abs slide-thumb right" width="135" height="140" viewBox="0 0 135 140">
    <polygon points="67,4 129,38 129,102 67,136 5,102 5,38" fill="#5f87a6" stroke="#fff" stroke-width="3" role="img" aria-label="Preview of next slide, harbour view"/>
    <circle cx="99" cy="70" r="17" fill="none" stroke="#fff" stroke-width="2.5"/>
    <path d="M95 62 L103 70 L95 78" fill="none" stroke="#fff" stroke-width="3"/>
  </svg>
  <svg class="abs scroll-down" width="60" height="62" viewBox="0 0 60 62">
    <polygon points="30,2 56,16 56,46 30,60 4,46 4,16" fill="none" stroke="#fff" stroke-width="3"/>
    <path d="M20 26 L30 36 L40 26" fill="none" stroke="#fff" stroke-width="3.5"/>
  </svg>
</section>

<section class="family">
  <h2 class="abs center slab-title">My family comes first</h2>
  <p class="abs center lead">I care for the environment – but not at the cost of my job,<br>our savings or our retirement</p>
  <a class="abs btn">Take action to protect your family</a>
</section>

<section class="features">
  <div class="photo" role="img" aria-label="Crowd of office workers standing together"></div>
  <h2 class="abs center slab-title">Features</h2>
  <p class="abs center lead">Tell your bank and super fund you do NOT want them to divest out of<br>Australian industry. Tell them you want to keep Australia strong</p>

  <div class="abs feature" style="left:147px;top:294px">
    <div class="hex-wrap">
      <svg width="130" height="150" viewBox="0 0 130 150"><polygon points="65,3 126,38 126,112 65,147 4,112 4,38" fill="none" stroke="#fff" stroke-width="3"/>
        <circle cx="65" cy="58" r="14" fill="none" stroke="#fff" stroke-width="3"/><circle cx="65" cy="58" r="5" fill="none" stroke="#fff" stroke-width="2.5"/>
        <g stroke="#fff" stroke-width="4"><line x1="65" y1="38" x2="65" y2="44"/><line x1="65" y1="72" x2="65" y2="78"/><line x1="45" y1="58" x2="51" y2="58"/><line x1="79" y1="58" x2="85" y2="58"/><line x1="51" y1="44" x2="55" y2="48"/><line x1="75" y1="68" x2="79" y2="72"/><line x1="79" y1="44" x2="75" y2="48"/><line x1="55" y1="68" x2="51" y2="72"/></g>
      </svg>
      <span class="hex-label">About</span>
    </div>
    <p>We really believe that apps and websites should not only be eye catching but an actually provide a really great user experience that users will be actually</p>
  </div>

  <div class="abs feature" style="left:376px;top:294px">
    <div class="hex-wrap">
      <svg width="130" height="150" viewBox="0 0 130 150"><polygon points="65,3 126,38 126,112 65,147 4,112 4,38" fill="none" stroke="#fff" stroke-width="3"/>
        <circle cx="65" cy="50" r="11" fill="none" stroke="#fff" stroke-width="3"/><path d="M44 80 Q44 64 65 64 Q86 64 86 80 Z" fill="none" stroke="#fff" stroke-width="3"/>
      </svg>
      <span class="hex-label">Team</span>
    </div>
    <p>We really believe that apps and websites should not only be eye catching but an actually provide a really great user experience that users will be actually</p>
  </div>

  <div class="abs feature" style="left:606px;top:294px">
    <div class="hex-wrap">
      <svg width="130" height="150" viewBox="0 0 130 150"><polygon points="65,3 126,38 126,112 65,147 4,112 4,38" fill="none" stroke="#fff" stroke-width="3"/>
        <path d="M50 78 L53 66 L75 42 L84 51 L62 75 Z M71 46 L80 55" fill="none" stroke="#fff" stroke-width="3" stroke-linejoin="round"/>
      </svg>
      <span class="hex-label">Blog</span>
    </div>
    <p>We really believe that apps and websites should not only be eye catching but an actually provide a really great user experience that users will be actually</p>
  </div>

  <div class="abs feature" style="left:836px;top:294px">
    <div class="hex-wrap">
      <svg width="130" height="150" viewBox="0 0 130 150"><polygon points="65,3 126,38 126,112 65,147 4,112 4,38" fill="none" stroke="#fff" stroke-width="3"/>
        <path d="M44 58 L86 40 L72 80 L63 63 Z M63 63 L86 40" fill="none" stroke="#fff" stroke-width="3" stroke-linejoin="round"/>
      </svg>
      <span class="hex-label">Contact</span>
    </div>
    <p>We really believe that apps and websites should not only be eye catching but an actually provide a really great user experience that users will be actually</p>
  </div>
</section>

<section class="about">
  <h2 class="abs center slab-title">About Enduring Progress</h2>
  <div class="abs video-frame" role="img" aria-label="Embedded campaign video, harbour and city skyline at sunset"></div>
  <div class="abs about-copy">
    <p>The Greenies want your bank and your super fund to stop investing in mining, agriculture and other industries that are the backbone of Australia.</p>
    <p>While they are trying to 'do good' if they are successful their actions will severely impact the lives of everyday Australians.  Any loss of investment in Australian industries WILL have knock on effects for you, your family and your community.</p>
  </div>
  <a class="abs btn">Lets Get Started</a>
</section>

<section class="email">
  <div class="photo" role="img" aria-label="Man with raised arms on a rooftop above a city skyline"></div>
  <h2 class="abs center slab-title">Email your bank</h2>
  <p class="abs lead">Take a few moments to contact your bank and let them know you do not want them to divest from Australian industry. Here's your opportunity to be heard. Your voice will make a difference.</p>

  <div class="abs field col-a" style="top:343px">NAME<svg width="12" height="12" viewBox="0 0 12 12"><circle cx="6" cy="4" r="2.6" fill="#8a94a0"/><path d="M1 12 Q1 7 6 7 Q11 7 11 12Z" fill="#8a94a0"/></svg></div>
  <div class="abs field col-b" style="top:343px">FAMILY NAME<svg width="12" height="12" viewBox="0 0 12 12"><circle cx="6" cy="4" r="2.6" fill="#8a94a0"/><path d="M1 12 Q1 7 6 7 Q11 7 11 12Z" fill="#8a94a0"/></svg></div>
  <div class="abs field col-a" style="top:394px">EMAIL<svg width="14" height="10" viewBox="0 0 14 10"><rect x="1" y="1" width="12" height="8" fill="none" stroke="#8a94a0" stroke-width="1.5"/><path d="M1 1 L7 6 L13 1" fill="none" stroke="#8a94a0" stroke-width="1.5"/></svg></div>
  <div class="abs field col-b" style="top:394px">BANK<svg width="10" height="6" viewBox="0 0 10 6"><path d="M1 1 L5 5 L9 1" fill="none" stroke="#8a94a0" stroke-width="1.6"/></svg></div>
  <div class="abs field col-a" style="top:448px">SUPER FUND<svg width="10" height="6" viewBox="0 0 10 6"><path d="M1 1 L5 5 L9 1" fill="none" stroke="#8a94a0" stroke-width="1.6"/></svg></div>
  <div class="abs submit col-b" style="top:448px;height:31px">SUBMIT</div>

  <div class="abs divider"></div>
  <div class="abs social"><span></span><span></span><span></span><span></span><span></span></div>
</section>

<section class="contact">
  <h2 class="abs center">Contact Us</h2>
  <h3 class="abs" style="left:193px">That's where we are</h3>
  <h3 class="abs" style="left:616px">It's easy to get started</h3>

  <div class="abs info" style="left:193px;top:278px">
    <svg width="24" height="22" viewBox="0 0 24 22"><path d="M2 4 L8 2 L16 4 L22 2 L22 18 L16 20 L8 18 L2 20 Z M8 2 L8 18 M16 4 L16 20" fill="none" stroke="#fff" stroke-width="1.6" stroke-linejoin="round"/></svg>
    <span class="label">LOCATION</span>14 Ridgeway Lane, Suite 3<br>Ballarat VIC 3350
  </div>
  <div class="abs info" style="left:403px;top:278px">
    <svg width="24" height="22" viewBox="0 0 24 22"><rect x="2" y="4" width="20" height="14" fill="none" stroke="#fff" stroke-width="1.6"/><path d="M2 4 L12 12 L22 4" fill="none" stroke="#fff" stroke-width="1.6"/></svg>
    <span class="label">EMAIL</span>hello@enduringprogress.org
  </div>
  <div class="abs info" style="left:193px;top:390px">
    <svg width="24" height="22" viewBox="0 0 24 22"><path d="M5 2 L9 2 L10 7 L7.5 9 Q10 14 14 15.5 L16 13 L21 14 L21 18 Q21 20 18 20 Q4 18 3 5 Q3 2 5 2 Z" fill="none" stroke="#fff" stroke-width="1.6" stroke-linejoin="round"/></svg>
    <span class="label">PHONE NUMBER</span>0400 123 456
  </div>
  <div class="abs info" style="left:403px;top:390px">
    <svg width="24" height="22" viewBox="0 0 24 22"><path d="M3 10 L7 10 L7 20 L3 20 Z M7 11 L11 3 Q14 3 13 8 L20 8 Q22 9 21 12 L19 19 Q18 20 16 20 L7 20" fill="none" stroke="#fff" stroke-width="1.6" stroke-linejoin="round"/></svg>
    <span class="label">SOCIAL MEDIA</span>@enduringprogress
  </div>

  <div class="abs field" style="left:616px;top:271px;width:401px">EMAIL<svg width="14" height="10" viewBox="0 0 14 10"><rect x="1" y="1" width="12" height="8" fill="none" stroke="#8a94a0" stroke-width="1.5"/><path d="M1 1 L7 6 L13 1" fill="none" stroke="#8a94a0" stroke-width="1.5"/></svg></div>
  <div class="abs field msg" style="left:616px;top:315px;width:401px">YOUR MESSAGE</div>
  <a class="abs btn">Send Messages</a>
</section>

</body>
</html>
```